Business card design needed

We do excavation, cartage and contracting
I would quote like to have a picture of my digger as the whole back ground and the words on top. If that looks any good
Otherwise please feel free to come up with any other cool options

Cheers Marc

KLR Contracting
Excavation, Cartage, Contracting
Marcus Prewitt
www.klr-example.co.nz
021 584 067
marc@klr-example.co.nz

```html
<!DOCTYPE html>
<html lang="en">
<head>
<meta charset="utf-8">
<title>KLR Contracting — Business Card</title>
<link href="https://fonts.googleapis.com/css2?family=Fira+Sans:wght@400&display=swap" rel="stylesheet">
<style>
  :root {
    --backdrop: #151515;
    --gold-light: #fedd8b;
    --gold-mid: #dcbc78;
    --gold-deep: #8c7547;
    --forest: #22552b;
  }
  * { margin: 0; padding: 0; box-sizing: border-box; }
  html, body {
    width: 1200px;
    height: 830px;
    overflow: hidden;
    background: var(--backdrop);
  }
  .business-card {
    position: absolute;
    left: 50px;
    top: 119px;
    width: 1100px;
    height: 592px;
    background:
      radial-gradient(ellipse 95% 120% at 52% 0%, var(--gold-light) 0%, var(--gold-mid) 45%, var(--gold-deep) 110%);
    color: var(--forest);
    font-family: "Fira Sans", sans-serif;
  }
  .brand-name {
    position: absolute;
    left: 96px;
    top: 167px;
    width: 358px;
    height: 258px;
    display: flex;
    align-items: center;
    justify-content: center;
    gap: 22px;
    font-size: 96px;
    font-weight: 400;
    letter-spacing: 2px;
    line-height: 1;
  }
  .brand-square {
    width: 26px;
    height: 26px;
    background: var(--forest);
  }
  .divider {
    position: absolute;
    left: 548px;
    top: 50px;
    width: 4px;
    height: 482px;
    background: var(--forest);
  }
  .contact-details {
    position: absolute;
    left: 618px;
    top: 140px;
    list-style: none;
    font-size: 33px;
    line-height: 51.2px;
    font-weight: 400;
    white-space: nowrap;
  }
</style>
</head>
<body>
  <div class="business-card">
    <div class="brand-name">
      <span class="brand-square"></span>
      <span>KLR</span>
    </div>
    <div class="divider"></div>
    <ul class="contact-details">
      <li class="company-line">KLR Contracting Excavation</li>
      <li class="service-line">Cartage</li>
      <li class="owner-line">Contracting Marcus Prewitt</li>
      <li class="website">www.klr-example.co.nz</li>
      <li class="phone">021 584 067</li>
      <li class="email">marc@klr-example.co.nz</li>
    </ul>
  </div>
</body>
</html>
```